#37- I like the envelope with only the logo on the back flap, no color. Also for the actual stationary I'm not sure if i like the purple & pink at the bottom. Maybe you can put my info along the bottom.
#31- can you use the same font I like for the front and back, also the same colors for the wording. I see the "weddings & events" is a diff color on either side.
I love #9, 26 & 27: For the hearts in the corners can you play around with standard hearts, I think using the logo so much is overwhelming. Also, try using the same font (feel script) for my name on both sides. I'm not sure if I like the different font for the front.
#27- I like how the heart is cut off, but can you cut off less of the heart? Also can you try putting the heart on a slant on the front? thanks!
Logo files have been uploaded in the creative brief.

```html
<!DOCTYPE html>
<html lang="en">
<head>
<meta charset="utf-8">
<title>Ethan Price – Weddings &amp; Events Business Cards</title>
<link rel="stylesheet" href="https://fonts.googleapis.com/css2?family=Italianno&family=Montserrat:wght@500&family=Roboto:wght@400&display=swap">
<style>
  :root {
    --backdrop: #4a3833;
    --card: #fbfafb;
    --plum: #5b2a6b;
    --plum-soft: #8a4c9a;
    --rose: #c2529a;
    --ink: #4a4a4a;
    --shadow: rgba(0, 0, 0, 0.35);
  }
  * { box-sizing: border-box; margin: 0; padding: 0; }
  html, body { width: 1200px; height: 995px; overflow: hidden; }
  body { background: var(--backdrop); position: relative; font-family: "Roboto", Arial, sans-serif; }

  .card {
    position: absolute;
    background: var(--card);
    border-radius: 16px;
    box-shadow: 0 6px 18px var(--shadow);
    overflow: hidden;
  }
  .card--front-landscape { left: 135px; top: 32px; width: 445px; height: 286px; }
  .card--back-landscape  { left: 599px; top: 94px; width: 464px; height: 240px; }
  .card--back-portrait   { left: 364px; top: 394px; width: 262px; height: 523px; }
  .card--front-portrait  { left: 655px; top: 410px; width: 254px; height: 512px; transform: rotate(-8deg); transform-origin: center; }

  .floral {
    position: absolute;
    border-radius: 50%;
    background: radial-gradient(ellipse at center, rgba(194, 82, 154, 0.32) 0%, rgba(138, 76, 154, 0.18) 45%, rgba(251, 250, 251, 0) 72%);
  }

  .brand {
    position: absolute;
    text-align: center;
    color: var(--plum);
  }
  .brand__name {
    font-family: "Italianno", cursive;
    font-size: 64px;
    line-height: 0.9;
    color: var(--plum);
  }
  .brand__tagline {
    font-family: "Montserrat", Arial, sans-serif;
    font-size: 11px;
    letter-spacing: 2px;
    text-transform: uppercase;
    color: var(--plum);
    margin-top: 6px;
  }

  .role-title {
    position: absolute;
    font-family: "Italianno", cursive;
    color: var(--plum);
    line-height: 0.85;
  }

  .contact-list { position: absolute; list-style: none; }
  .contact-list li {
    display: flex; align-items: center; gap: 8px;
    font-size: 13px; color: var(--ink); margin-bottom: 6px;
  }
  .contact-list svg { width: 14px; height: 14px; flex: none; }
</style>
</head>
<body>

  <!-- Landscape front -->
  <section class="card card--front-landscape">
    <div class="floral" role="img" aria-label="Pink and purple floral swirl ornament around the name" style="left:40px; top:10px; width:370px; height:270px;"></div>
    <div class="brand" style="left:0; right:0; top:92px;">
      <div class="brand__name">Ethan Price</div>
      <div class="brand__tagline">Weddings &amp; Events</div>
    </div>
  </section>

  <!-- Landscape back -->
  <section class="card card--back-landscape">
    <div class="floral" role="img" aria-label="Small purple floral corner ornament" style="left:330px; top:-20px; width:160px; height:120px;"></div>
    <div class="brand" style="left:18px; top:70px; text-align:left;">
      <div class="brand__name" style="font-size:50px;">Ethan<br>Price</div>
    </div>
    <div class="role-title" style="left:228px; top:40px; font-size:58px;">Event<br>&nbsp;&nbsp;Planner</div>
    <ul class="contact-list" style="left:232px; top:166px;">
      <li><svg viewBox="0 0 16 16"><circle cx="8" cy="8" r="8" fill="var(--plum)"/><path d="M5 4.5c.6 3 2.8 5.8 6 7l1-1.6-1.8-1-1 .8C8 9 7 8 6.3 6.8l.8-1-1-1.8z" fill="#fff"/></svg>914 555 0142</li>
      <li><svg viewBox="0 0 16 16"><circle cx="8" cy="8" r="8" fill="var(--plum)"/><rect x="4" y="5" width="8" height="6" fill="none" stroke="#fff" stroke-width="1.2"/><path d="M4 5l4 3.5L12 5" fill="none" stroke="#fff" stroke-width="1.2"/></svg>ethan@ethanpriceevents.com</li>
      <li><svg viewBox="0 0 16 16"><circle cx="8" cy="8" r="8" fill="var(--plum)"/><circle cx="8" cy="8" r="4" fill="none" stroke="#fff" stroke-width="1.1"/><path d="M4 8h8M8 4c-2 2.5-2 5.5 0 8M8 4c2 2.5 2 5.5 0 8" fill="none" stroke="#fff" stroke-width="0.9"/></svg>www.ethanpriceevents.com</li>
    </ul>
  </section>

  <!-- Portrait back -->
  <section class="card card--back-portrait">
    <div class="brand" style="left:30px; right:0; top:90px;">
      <div class="brand__name" style="font-size:60px;">Ethan<br>&nbsp;&nbsp;Price</div>
    </div>
    <ul class="contact-list" style="left:30px; top:368px;">
      <li><svg viewBox="0 0 16 16"><circle cx="8" cy="8" r="8" fill="var(--plum)"/><path d="M5 4.5c.6 3 2.8 5.8 6 7l1-1.6-1.8-1-1 .8C8 9 7 8 6.3 6.8l.8-1-1-1.8z" fill="#fff"/></svg>914 555 0142</li>
      <li><svg viewBox="0 0 16 16"><circle cx="8" cy="8" r="8" fill="var(--plum)"/><rect x="4" y="5" width="8" height="6" fill="none" stroke="#fff" stroke-width="1.2"/><path d="M4 5l4 3.5L12 5" fill="none" stroke="#fff" stroke-width="1.2"/></svg>ethan@ethanpriceevents.com</li>
      <li><svg viewBox="0 0 16 16"><circle cx="8" cy="8" r="8" fill="var(--plum)"/><circle cx="8" cy="8" r="4" fill="none" stroke="#fff" stroke-width="1.1"/><path d="M4 8h8M8 4c-2 2.5-2 5.5 0 8M8 4c2 2.5 2 5.5 0 8" fill="none" stroke="#fff" stroke-width="0.9"/></svg>www.ethanpriceevents.com</li>
    </ul>
    <div class="floral" role="img" aria-label="Purple floral corner ornament" style="left:-30px; top:430px; width:190px; height:130px;"></div>
  </section>

  <!-- Portrait front -->
  <section class="card card--front-portrait">
    <div class="floral" role="img" aria-label="Pink and purple floral swirl ornament around the name" style="left:-30px; top:10px; width:310px; height:260px;"></div>
    <div class="brand" style="left:0; right:0; top:100px;">
      <div class="brand__name" style="font-size:50px;">Ethan Price</div>
      <div class="brand__tagline" style="font-size:9px;">Weddings &amp; Events</div>
    </div>
    <div class="role-title" style="left:70px; top:392px; font-size:50px;">Event<br>&nbsp;&nbsp;Planner</div>
  </section>

</body>
</html>
```